Business Card Design Harbor of Calm

mental health provider
contemporary
warmth
inviting

Target Market(s)

mental health clients adults

Industry/Entity Type

Mental Health

Contact Information for Business Card

Danielle Arkwright PMHNP
2841 SW Tenley Ave
Suite 384C
Portland OR 97318
Fax 503-555-0182
Tel 503-555-0147
Email danielle@darkwright.example
Website darkwright.example

Requirements
Nice to have
• see above
Should not have
• no medical logos

```html
<!DOCTYPE html>
<html lang="en">
<head>
<meta charset="utf-8">
<title>Harbor of Calm – Business Card</title>
<link href="https://fonts.googleapis.com/css2?family=Alegreya:wght@700&family=Lato:wght@400;700&display=swap" rel="stylesheet">
<style>
  :root {
    --canvas: #e6e6e3;
    --brown: #2c2116;
    --band: #a9cf6b;
    --leaf: #d2e8a6;
    --ink: #b4d77f;
    --shadow: rgba(0,0,0,0.28);
  }
  html, body { margin: 0; padding: 0; overflow: hidden; }
  body {
    width: 1200px; height: 1000px;
    background: var(--canvas);
    position: relative;
    font-family: "Lato", sans-serif;
  }
  .card {
    position: absolute;
    width: 700px; height: 400px;
    box-shadow: 0 10px 24px var(--shadow);
    overflow: hidden;
  }
  .card-front { left: 80px; top: 70px; }
  .card-back  { left: 420px; top: 530px; }
  .card-art { position: absolute; inset: 0; }
  .name-script {
    font-family: "Alegreya", serif;
    font-weight: 700;
    color: var(--ink);
    margin: 0;
  }
  .front-content {
    position: absolute;
    left: 40px; top: 70px;
    width: 440px;
    text-align: center;
    color: var(--ink);
  }
  .brand-row {
    display: flex; align-items: center; justify-content: center; gap: 14px;
  }
  .brand-dot {
    width: 30px; height: 30px; border-radius: 50%;
    background: var(--ink);
  }
  .front-content .name-script { font-size: 36px; line-height: 1.1; }
  .brand-sub { font-size: 28px; margin-top: 2px; }
  .contact-list {
    margin-top: 26px;
    font-size: 16.5px; line-height: 1.55;
  }
  .contact-list b { font-weight: 700; }
  .back-content {
    position: absolute;
    right: 40px; top: 86px;
    text-align: right;
    color: var(--ink);
  }
  .back-content .name-script { font-size: 29px; }
  .role { font-size: 19px; margin-top: 6px; }
  .phones { margin-top: 32px; font-size: 19px; line-height: 1.45; }
  .phones b { font-weight: 700; }
  .address { margin-top: 30px; font-size: 19px; line-height: 1.45; }
</style>
</head>
<body>

<section class="card card-front">
  <svg class="card-art" viewBox="0 0 700 400" width="700" height="400">
    <rect width="700" height="400" fill="var(--leaf)" role="img" aria-label="Soft light green floral pattern"/>
    <path d="M0 0 H380 C600 50 690 220 620 400 H0 Z" fill="var(--band)"/>
    <path d="M0 0 H320 C540 50 630 220 560 400 H0 Z" fill="var(--brown)"/>
  </svg>
  <div class="front-content">
    <div class="brand-row">
      <span class="brand-dot"></span>
      <p class="name-script">Danielle Arkwright</p>
    </div>
    <p class="name-script brand-sub">PMHNP, Inc.</p>
    <div class="contact-list">
      <div><b>Email:</b> danielle@darkwright.example</div>
      <div>Rosalind@darkwright.example (Billing Specialist)</div>
      <div>Tamsin@darkwright.example (Office Manager)</div>
      <div><b>Website:</b> www.darkwright.example</div>
    </div>
  </div>
</section>

<section class="card card-back">
  <svg class="card-art" viewBox="0 0 700 400" width="700" height="400">
    <rect width="700" height="400" fill="var(--leaf)" role="img" aria-label="Soft light green floral pattern"/>
    <path d="M700 0 H380 C290 70 280 250 300 400 H700 Z" fill="var(--band)"/>
    <path d="M700 0 H430 C350 70 335 250 350 400 H700 Z" fill="var(--brown)"/>
  </svg>
  <div class="back-content">
    <p class="name-script">Danielle Arkwright</p>
    <div class="role">PMHNP</div>
    <div class="phones">
      <div><b>Phone:</b> 503-555-0147</div>
      <div><b>Fax:</b> 503-555-0182</div>
    </div>
    <div class="address">
      <div>2841 SW Tenley Ave Suite 384C</div>
      <div>Portland OR 97318</div>
    </div>
  </div>
</section>

</body>
</html>
```